WWW.VELTRONA.IT BUSINNES CARD

WE NEED A BUSINESS CARD . I HAVE A COMPANY IN ITALY NR 1 IN HAIR MEDICAL CARE AN HAIR REPLECEMENT . IN CARD I NEED WRITE WEB ADDRESS, MAIL , ADDRESS, TELEPHONE NUMBER , AND NAME
IN THE BACK SIDE I NEED MY DOCTOR LOGO .
MY WEB SITE IS WWW.VELTRONA.IT
Updates

Target Market(s)

CONSUMER B2C

Industry/Entity Type

Hair And Beauty

Contact Information for Business Card

I WANT A MEDICAL BUSINESS CARD.

Font styles to use
Other font styles liked:
• VERDANA

Colors
33a6d7
3176b5
85abd2
aedbee
eaf1f7
ffffff

Requirements
Must have
• I NEED MY LOGO AND LOGO OF DR VELTRONA

```html
<!DOCTYPE html>
<html lang="it">
<head>
<meta charset="utf-8">
<title>Veltrona – Business Card</title>
<link rel="stylesheet" href="https://fonts.googleapis.com/css2?family=Open+Sans:wght@400;600;700&display=swap">
<style>
  :root {
    --stage: #3a3431;
    --card: #141516;
    --card-edge: #1c1d1f;
    --blue-bright: #33a6d7;
    --blue-deep: #3176b5;
    --blue-soft: #85abd2;
    --blue-pale: #aedbee;
    --text-light: #eaf1f7;
    --white: #ffffff;
    --mascot-brown: #6e4a33;
    --mascot-base: #a8785a;
  }
  * { box-sizing: border-box; margin: 0; padding: 0; }
  html, body {
    width: 1200px; height: 864px; overflow: hidden;
    background: var(--stage);
    font-family: "Open Sans", Verdana, sans-serif;
  }
  .canvas {
    position: relative; width: 1200px; height: 864px;
  }
  .card {
    position: absolute; top: 277px;
    width: 540px; height: 310px;
    background: linear-gradient(160deg, var(--card-edge), var(--card));
    border-radius: 4px;
    box-shadow: 0 18px 40px rgba(0,0,0,.45);
    overflow: hidden;
  }
  .card--back { left: 40px; }
  .card--front { left: 620px; }

  .mascot {
    position: absolute; left: 170px; top: 40px;
    width: 200px; height: 230px;
    border-radius: 50% 50% 46% 46% / 30% 30% 70% 70%;
    background: radial-gradient(ellipse at 50% 75%, var(--mascot-base) 0%, var(--mascot-brown) 55%, rgba(20,21,22,0) 75%);
    opacity: .85;
  }

  .brand {
    position: absolute; left: 34px; top: 104px; width: 260px;
  }
  .brand__row { display: flex; align-items: center; gap: 10px; }
  .brand__dot {
    width: 26px; height: 26px; border-radius: 50%;
    background: var(--blue-bright);
  }
  .brand__name {
    font-size: 36px; font-weight: 700; color: var(--blue-bright);
    letter-spacing: .5px; line-height: 1;
  }
  .brand__tagline {
    margin-top: 8px;
    font-size: 9.5px; font-weight: 400; color: var(--blue-soft);
    letter-spacing: .6px; text-transform: uppercase; white-space: nowrap;
  }
  .brand__swoosh { position: absolute; left: -8px; top: 66px; }

  .divider {
    position: absolute; left: 312px; top: 60px;
    width: 1px; height: 190px;
    background: linear-gradient(to bottom, rgba(255,255,255,0), rgba(255,255,255,.6), rgba(255,255,255,0));
  }

  .contact {
    position: absolute; left: 334px; top: 78px; width: 200px;
    color: var(--text-light); font-size: 13px; line-height: 1.45;
  }
  .contact__name {
    font-size: 17px; font-weight: 700; color: var(--blue-deep);
    margin-bottom: 12px;
  }
  .contact__address { margin-bottom: 6px; }
  .contact__list { list-style: none; }
  .contact__item { display: flex; align-items: center; gap: 8px; }
  .contact__icon { width: 12px; height: 12px; flex: none; fill: var(--blue-deep); }
</style>
</head>
<body>
<main class="canvas">

  <section class="card card--back" aria-label="Card back">
    <div class="mascot" role="img" aria-label="Doctor mascot illustration: a cartoon hair strand character in a lab coat standing on a round base"></div>
  </section>

  <section class="card card--front" aria-label="Card front">
    <div class="brand">
      <div class="brand__row">
        <span class="brand__dot"></span>
        <span class="brand__name">Veltrona</span>
      </div>
      <p class="brand__tagline">Cura e reintegrazione dei capelli</p>
      <svg class="brand__swoosh" width="250" height="40" viewBox="0 0 250 40">
        <path d="M4 6 C 70 36, 160 40, 246 26" fill="none" stroke="var(--blue-bright)" stroke-width="2"/>
      </svg>
    </div>

    <div class="divider"></div>

    <div class="contact">
      <p class="contact__name">Luca Ferrante</p>
      <p class="contact__address">Via delle Rose 112<br>50123 Firenze, Italy</p>
      <ul class="contact__list">
        <li class="contact__item">
          <svg class="contact__icon" viewBox="0 0 24 24"><path d="M6.6 10.8a15.1 15.1 0 0 0 6.6 6.6l2.2-2.2a1 1 0 0 1 1-.25 11.4 11.4 0 0 0 3.6.57 1 1 0 0 1 1 1V20a1 1 0 0 1-1 1A17 17 0 0 1 3 4a1 1 0 0 1 1-1h3.5a1 1 0 0 1 1 1c0 1.25.2 2.45.57 3.6a1 1 0 0 1-.25 1z"/></svg>
          <span>800562918</span>
        </li>
        <li class="contact__item">
          <svg class="contact__icon" viewBox="0 0 24 24"><path d="M2 5h20v14H2z M3 6l9 7 9-7" stroke="var(--card)" stroke-width="1.5"/></svg>
          <span>luca@veltrona.it</span>
        </li>
        <li class="contact__item">
          <svg class="contact__icon" viewBox="0 0 24 24"><circle cx="12" cy="12" r="10"/><path d="M2 12h20M12 2c3 3 3 17 0 20M12 2c-3 3-3 17 0 20" fill="none" stroke="var(--card)" stroke-width="1.5"/></svg>
          <span>www.veltrona.it</span>
        </li>
      </ul>
    </div>
  </section>

</main>
</body>
</html>
```